PowerPoint Design Project

Powerpoint design for an online marketing agency.
PP will be used as a WhitePaper to showcase our expertise.
Our USP is that we use data for marketing so the design must reflect this with charts and graphs.
A set of images is available in our flickr account
http://www.pixelvault.example/photos/kelmora/sets/48302916574021983/with/3104827561/
We already have written real content for the PP for you to work with.
Updates

1. I have added a sample of the content a 2-page extract in a word document. The full document is around 15 pages.
2. While the finished piece is to be in PowerPoint format, it will also be used as a White Paper so the design should reflect this - i.e it should be able to be read like it was a well designed Word document not just a PP
3. The design you see in the sample 2-page document is just for illustration purposes it is not intended to influence the final design at all. So for example it currently has some pull-quotes in black boxes - that is just to show what they are and I don't want the final piece to have black boxes around quotes.
4. I've been asked to make this project guaranteed: as this is the first time I've used ArtHivePro I'm going to keep it as a standard project but we are committed to the work.
5. The current deadline is for the START of design work. We need the completed design by 21 September, so there is plenty of time to schedule this in with your other work.
Many thanks
Nigel 

The designs shown so far would not be suitable for turning into a WhitePaper. For example the bars across the top of the design create a break at the start of each page rather than emphasise the continuous nature of the document. 

Here is an example of some great design for a similar project - and we've uploaded another sample as a file

http://www.surgeloft.example/downloads/[SURGE]-what-its-like-working-

If you asked me for some ideas on the feel of the design I would say:

1. Bold - it has to look interesting - corporate world but it doesn't need to feel dull/grey
2. Exciting 
3. Precise - easy to read , not a fussy design

Target Market(s)

Business developers, sales managers, CEOs of companies with over 5 employees but without their own marketing department

Industry/Entity Type

Marketing

Requirements
Must have
• Flawless design that says "this company is smart and means business"
Nice to have
• the powerpoint should lend itself to easy file/saveas to be delivered as a PDF and for individual slides to be extracted for presentation, or use as images in blog posts etc (so for example any page number must be easy to remove).
Should not have
• no cartoons, no line drawings, nothing to obscure easy legibility

```html
<!DOCTYPE html>
<html lang="en">
<head>
<meta charset="utf-8">
<title>Create remarkable content that people want to receive and share</title>
<link href="https://fonts.googleapis.com/css2?family=Carlito:ital,wght@0,400;0,700;1,400&display=swap" rel="stylesheet">
<style>
  :root {
    --ink: #1a1a1a;
    --heading: #1f3f7a;
    --page: #ffffff;
    --page-edge: #b9b9b9;
    --chart-frame: #8c8c8c;
    --grid: #d9d9d9;
    --note-border: #2f6fc0;
    --note-bg: #1f5fb3;
    --quote-bg: #e6e9ef;
    --quote-bar: #1f5fb3;
    --photo-top: #d8dde3;
    --photo-bottom: #6f7b88;
    --bar-1: #3f6fc4;
    --bar-2: #c0504d;
    --bar-3: #9bbb59;
    --bar-4: #8064a2;
    --bar-5: #4bacc6;
    --bar-6: #f79646;
    --bar-7: #8fb4e3;
    --bar-8: #e6a6a5;
    --bar-9: #c5b8da;
    --bar-10: #cfe0a8;
  }
  html, body { margin: 0; padding: 0; overflow: hidden; background: #f2f2f2; }
  .page {
    position: relative;
    width: 900px; height: 1200px;
    box-sizing: border-box;
    background: var(--page);
    border: 2px solid var(--page-edge);
    font-family: "Carlito", Calibri, sans-serif;
    color: var(--ink);
    overflow: hidden;
  }
  .page-title {
    position: absolute; left: 40px; top: 26px; width: 820px;
    margin: 0; font-size: 26px; font-weight: 700; color: var(--heading);
  }
  .intro {
    position: absolute; left: 40px; top: 96px; width: 640px;
    font-size: 18.5px; line-height: 1.3;
  }
  .intro p { margin: 0 0 4px; }
  .intro ul { margin: 0; padding-left: 28px; }
  .intro li { margin-bottom: 2px; }
  .chart-panel {
    position: absolute; left: 62px; top: 350px; width: 628px; height: 388px;
    box-sizing: border-box; border: 2px solid var(--chart-frame);
    background: var(--page);
  }
  .chart-panel svg { position: absolute; left: 0; top: 0; }
  .chart-note {
    position: absolute; left: 322px; top: 14px; width: 278px;
    box-sizing: border-box; padding: 10px 12px;
    background: var(--note-bg); border: 2px solid var(--note-border);
    color: #ffffff; font-size: 14px; line-height: 1.25;
  }
  .chart-note p { margin: 0 0 6px; }
  .chart-note ul { margin: 0 0 6px; padding: 0; list-style: none; }
  .chart-note .source { font-size: 9px; margin: 0; }
  .axis-label { font-size: 11px; fill: #333; font-family: "Carlito", Calibri, sans-serif; }
  .presenter-photo {
    position: absolute; left: 700px; top: 560px; width: 180px; height: 520px;
    background: linear-gradient(180deg, var(--photo-top), var(--photo-bottom));
    border-radius: 90px 90px 10px 10px;
  }
  .science-line {
    position: absolute; left: 40px; top: 744px; width: 640px;
    margin: 0; font-size: 18.5px; line-height: 1.3;
  }
  .pull-quote {
    position: absolute; left: 62px; top: 830px; width: 590px;
    box-sizing: border-box; padding: 12px 16px 12px 20px;
    background: var(--quote-bg); border-left: 6px solid var(--quote-bar);
    margin: 0; font-size: 18.5px; font-style: italic; line-height: 1.3;
  }
  .pull-quote .mark { color: var(--quote-bar); font-size: 26px; font-weight: 700; }
  .closing {
    position: absolute; left: 40px; top: 950px; width: 640px;
    margin: 0; font-size: 18.5px; line-height: 1.3;
  }
  .copyright {
    position: absolute; left: 14px; top: 1166px;
    margin: 0; font-size: 11px; color: #444;
  }
</style>
</head>
<body>
<div class="page">
  <h1 class="page-title">Create remarkable content that people want to receive and share</h1>

  <div class="intro">
    <p>The modern science of marketing uses a new and scientific approach to the way businesses market their products for profit. Combining marketing expertise, statistical data, and psychological research from behavioural economics, the science of marketing explains how companies can use 21<sup>st</sup> century marketing strategies like blogging, social media and permission-based email marketing to:</p>
    <ul>
      <li>know what works in marketing, based on interpreting measurable statistical data</li>
      <li>target marketing budgets for highest impact using evidence of return on investment</li>
      <li>adapt marketing campaigns in real-time based on actual customer behaviour.</li>
    </ul>
  </div>

  <div class="chart-panel">
    <svg width="624" height="384" viewBox="0 0 624 384" role="img" aria-label="Bar chart of views by headline word">
      <g stroke="var(--grid)" stroke-width="1">
        <line x1="40" y1="330" x2="600" y2="330"/>
        <line x1="40" y1="285.7" x2="600" y2="285.7"/>
        <line x1="40" y1="241.4" x2="600" y2="241.4"/>
        <line x1="40" y1="197.1" x2="600" y2="197.1"/>
        <line x1="40" y1="152.9" x2="600" y2="152.9"/>
        <line x1="40" y1="108.6" x2="600" y2="108.6"/>
        <line x1="40" y1="64.3" x2="600" y2="64.3"/>
        <line x1="40" y1="20" x2="600" y2="20"/>
      </g>
      <line x1="40" y1="20" x2="40" y2="330" stroke="#999"/>
      <g class="axis-label" text-anchor="end">
        <text x="34" y="334">0</text>
        <text x="34" y="290">100</text>
        <text x="34" y="245">200</text>
        <text x="34" y="201">300</text>
        <text x="34" y="157">400</text>
        <text x="34" y="113">500</text>
        <text x="34" y="68">600</text>
        <text x="34" y="24">700</text>
      </g>
      <rect x="51" y="42.1" width="34" height="287.9" fill="var(--bar-1)"/>
      <rect x="107" y="73.1" width="34" height="256.9" fill="var(--bar-2)"/>
      <rect x="163" y="219.3" width="34" height="110.7" fill="var(--bar-3)"/>
      <rect x="219" y="219.3" width="34" height="110.7" fill="var(--bar-4)"/>
      <rect x="275" y="219.3" width="34" height="110.7" fill="var(--bar-5)"/>
      <rect x="331" y="241.4" width="34" height="88.6" fill="var(--bar-6)"/>
      <rect x="387" y="263.6" width="34" height="66.4" fill="var(--bar-7)"/>
      <rect x="443" y="263.6" width="34" height="66.4" fill="var(--bar-8)"/>
      <rect x="499" y="303.4" width="34" height="26.6" fill="var(--bar-9)"/>
      <rect x="555" y="307.9" width="34" height="22.1" fill="var(--bar-10)"/>
      <g class="axis-label" text-anchor="middle">
        <text x="68" y="348">insights</text>
        <text x="124" y="348">analysis</text>
        <text x="180" y="348">answers</text>
        <text x="236" y="348">questions</text>
        <text x="292" y="348">where</text>
        <text x="348" y="348">review</text>
        <text x="404" y="348">why</text>
        <text x="460" y="348">product</text>
        <text x="516" y="348">top</text>
        <text x="572" y="348">best</text>
      </g>
    </svg>
    <div class="chart-note">
      <p>The most popular words for attracting views to social media content like blogs or video (in other words, imply &ldquo;thought leadership&rdquo;) including phrases like:</p>
      <ul>
        <li>- insights</li>
        <li>- analysis</li>
        <li>- answers</li>
        <li>- questions.</li>
      </ul>
      <p class="source">Source: keyword study, http://www.example.test/word-views</p>
    </div>
  </div>

  <div class="presenter-photo" role="img" aria-label="Photo of a cheering businessman in a suit, arms raised"></div>

  <p class="science-line">The science of marketing gives you the research and tools to deliver scientific marketing that works, based on data you can prove.</p>

  <blockquote class="pull-quote"><span class="mark">&ldquo;</span>No longer are size and budget the deciding factors. Now speed and agility are decisive competitive advantage &ndash; Harlan Whitby</blockquote>

  <p class="closing">Now you know what the science of marketing is, how can you design a marketing campaign that (to use an Americanism) rocks your ROI?</p>

  <p class="copyright">&copy;2012 Kelmora and or it&rsquo;s affiliates. All Rights Reserved.</p>
</div>
</body>
</html>
```